Stationary Project for Single Designer: Pinto Visual Design Agency

Stationary Project for single Designer: Pinto Visual Design Agency (http://artists.sketchhive.example/artist/52714)
As per previous discussion.
Business Stationary ($160)
Business card Wellquarta
Business Card Tender Harbour
In addition to the current deign you provided can we see one where you have the logo and the name along side the logo ie like the logo in design 4187396
Letter head Wellquarta
Letter Head Tender Harbour
Power point template Wellquarta
Address is: 7, Jalan Merbuk 3C, Taman Kenanga, 43310 Seri Kembangan, Selangor
For the business card will need phone number space for Malaysia and Australia
Development of Style Manual ($100)
Let me know if you want more detail
Sorry this was meant to be a job for a specific designer. Not sure how this went out to a competition format.

```html
<!DOCTYPE html>
<html lang="en">
<head>
<meta charset="utf-8">
<title>Business Cards — Wellquarta &amp; Tender Harbour</title>
<link rel="stylesheet" href="https://fonts.googleapis.com/css2?family=Montserrat:wght@400;500;700&display=swap">
<style>
  :root {
    --purple: #6a2180;
    --orange: #f39200;
    --page: #ffffff;
    --card: #ffffff;
    --shadow: rgba(0, 0, 0, 0.28);
  }
  * { margin: 0; padding: 0; box-sizing: border-box; }
  html, body {
    width: 1200px;
    height: 831px;
    overflow: hidden;
    background: var(--page);
  }
  .sheet {
    position: relative;
    width: 1200px;
    height: 831px;
    font-family: "Montserrat", sans-serif;
    color: var(--purple);
  }
  .card {
    position: absolute;
    width: 527px;
    height: 338px;
    background: var(--card);
    box-shadow: 0 1px 5px var(--shadow);
    overflow: hidden;
  }
  .card--front.row-1 { left: 51px; top: 55px; }
  .card--back.row-1  { left: 622px; top: 55px; }
  .card--front.row-2 { left: 51px; top: 439px; }
  .card--back.row-2  { left: 622px; top: 439px; }

  .brand {
    position: absolute;
    left: 34px;
    top: 44px;
    display: flex;
    align-items: center;
    gap: 10px;
  }
  .brand__dot {
    width: 54px;
    height: 54px;
    border-radius: 50%;
    background: var(--orange);
    flex: none;
  }
  .brand__text { display: flex; flex-direction: column; }
  .brand__name {
    font-size: 27px;
    font-weight: 700;
    letter-spacing: -0.6px;
    color: var(--purple);
    line-height: 1;
  }
  .brand__parent {
    align-self: flex-end;
    font-size: 10px;
    font-weight: 500;
    margin-top: 3px;
    color: var(--purple);
  }

  .person {
    position: absolute;
    left: 35px;
    top: 150px;
  }
  .person__name {
    font-size: 16px;
    font-weight: 700;
    line-height: 1.1;
  }
  .person__role {
    font-size: 12.5px;
    font-weight: 400;
    margin-top: 2px;
  }

  .contact {
    position: absolute;
    left: 242px;
    top: 153px;
    font-size: 12.5px;
    font-weight: 400;
    line-height: 15.6px;
    list-style: none;
  }
  .contact__row { display: flex; }
  .contact__label { width: 18px; flex: none; }
  .contact__gap { height: 15.6px; }
  .contact__web {
    position: absolute;
    left: 242px;
    top: 290px;
    font-size: 15px;
    font-weight: 700;
  }

  .card__pattern {
    position: absolute;
    inset: 0;
    background:
      radial-gradient(circle at 30% 30%, rgba(243,146,0,0.85) 0 22%, transparent 40%),
      radial-gradient(circle at 75% 70%, rgba(106,33,128,0.85) 0 22%, transparent 42%),
      linear-gradient(135deg, #f7b24a 0%, #ffffff 50%, #8a4aa0 100%);
  }
</style>
</head>
<body>
<main class="sheet">

  <section class="card card--front row-1">
    <div class="brand">
      <span class="brand__dot"></span>
      <div class="brand__text">
        <span class="brand__name">Wellquarta</span>
      </div>
    </div>
    <div class="person">
      <p class="person__name">Name Surname</p>
      <p class="person__role">Executive Director</p>
    </div>
    <ul class="contact">
      <li class="contact__row"><span class="contact__label">A :</span><span>7 Jalan Merbuk 3C</span></li>
      <li class="contact__row"><span class="contact__label"></span><span>Taman Kenanga</span></li>
      <li class="contact__row"><span class="contact__label"></span><span>43310 Seri Kembangan</span></li>
      <li class="contact__row"><span class="contact__label"></span><span>Selangor, Malaysia</span></li>
      <li class="contact__gap"></li>
      <li class="contact__row"><span class="contact__label">T :</span><span>+00 0000 0000 (MY)</span></li>
      <li class="contact__row"><span class="contact__label">T :</span><span>+000 0000 0000 (AU)</span></li>
      <li class="contact__row"><span class="contact__label">E :</span><span>name.surname@wellquarta.com</span></li>
    </ul>
    <p class="contact__web">www.wellquarta.com</p>
  </section>

  <section class="card card--back row-1">
    <div class="card__pattern" role="img" aria-label="Large cropped brand symbol in purple and orange filling the card back"></div>
  </section>

  <section class="card card--front row-2">
    <div class="brand">
      <span class="brand__dot"></span>
      <div class="brand__text">
        <span class="brand__name">Tender Harbour</span>
        <span class="brand__parent">by Wellquarta</span>
      </div>
    </div>
    <div class="person">
      <p class="person__name">Name Surname</p>
      <p class="person__role">Executive Director</p>
    </div>
    <ul class="contact">
      <li class="contact__row"><span class="contact__label">A :</span><span>7 Jalan Merbuk 3C</span></li>
      <li class="contact__row"><span class="contact__label"></span><span>Taman Kenanga</span></li>
      <li class="contact__row"><span class="contact__label"></span><span>43310 Seri Kembangan</span></li>
      <li class="contact__row"><span class="contact__label"></span><span>Selangor, Malaysia</span></li>
      <li class="contact__gap"></li>
      <li class="contact__row"><span class="contact__label">T :</span><span>+00 0000 0000 (MY)</span></li>
      <li class="contact__row"><span class="contact__label">T :</span><span>+000 0000 0000 (AU)</span></li>
      <li class="contact__row"><span class="contact__label">E :</span><span>name.surname@tenderharbour.com</span></li>
    </ul>
    <p class="contact__web">www.tenderharbour.com</p>
  </section>

  <section class="card card--back row-2">
    <div class="card__pattern" role="img" aria-label="Large cropped brand symbol in purple and orange filling the card back"></div>
  </section>

</main>
</body>
</html>
```